Brochure Design Project (Design Studio)

Items required:
1-Brochure. We suggest 15Cm X 15 Cm after cutting.
2-Business Card.
3-Head letter.
4-Folder ( folder should carry the Brochure in pocket and the business card in a pocket on the opposite side of the folder.
5-Envelope to carry everything.
This brochure is expected to draw attention of high level management in companies to the quality and creativity of the design work and encourage them to do business with us. note that brochure will be printed in high quality printing and paper.
The game plan is as follows:
Over all description, the theme of the brochure is drawn from the website theme (website will be uploaded shortly, pictures of the website are attached, logo appears in the top left corner). Please avoid direct copying from the website unless it is a creative copying, just draw the theme from there. however, we need it to be elegant, stylish and class in colors and style. This is a MUST.
Furthermore, the main items of the Brochure:
1-The Studio is not just a studio: we will take about how Branding. A file is attached of the content. (slight changes/modification can apply during the designing process)
2-The Process: this one has to be a visual illustration of the process, it has to be very creative, could be elegant arrows and comics, could be elegant drawing, could be an elegant icons. The drawing should be separate from the steps, we need to the drawing and we need to have the steps listed and commentary, or if want to integrate both in one in an artistic way. Just don’t lose track of the theme and elegance. (steps and commentary are attached, slight changes/modification can apply at anytime.
3-Our Team: another drawing of your suggestion to illustrate the team members, we need to include the names and designation as well leave a place for some of them to say what they need to say about their style of designing. I leave it for your imagination to put this all together in a nice attractive visual illustration.
4-Works: this section will generally show the works of our designers. It needs to be focused on the works themselves, client should be able to view the details of the works ( note that when it comes to brochures and websites, we don’t need to reach to the extent with which the client can read the text in those pictures of the website or brochure, but still can see the overall design clearly). Each design is to carry the name of the designer. Last thing, this section will classify works into categories, like, Brochures, Corporate identity, print design. We didn’t finalize those categories, we will provide them to you shortly, last thing to be said, we are planning to include around 25-30 designs of each sub-category, eg. Corporate identity will have 30 business card s designs and 30 stationary designs.
5-Contacts: the company contacts.
We the brochure after printing should be 15x15 Cm.
Creativity and art work is a major player in selection.
general managers, owners
Printing

```html
<!DOCTYPE html>
<html lang="en">
<head>
<meta charset="utf-8">
<title>Lumera Creative Studio – Business Card</title>
<link rel="stylesheet" href="https://fonts.googleapis.com/css2?family=Francois+One&family=Pathway+Gothic+One&family=Arimo&family=Pinyon+Script&display=swap">
<style>
  :root {
    --page-bg: #dcdcde;
    --card-dark: #1c1d1c;
    --card-mid: #3a3a36;
    --accent: #f05a2a;
    --rust-dark: #4e1708;
    --rust-light: #a24a31;
    --rule: #b9b9b9;
    --white: #ffffff;
    --tagline: #cfcfcf;
    --ink: #111111;
  }
  html, body {
    margin: 0;
    width: 1200px;
    height: 1200px;
    overflow: hidden;
    background: var(--page-bg);
  }
  .business-card {
    position: absolute;
    left: 138px;
    top: 296px;
    width: 894px;
    height: 568px;
    border-radius: 40px;
    border: 3px solid var(--white);
    box-sizing: border-box;
    overflow: hidden;
    background: radial-gradient(ellipse at 62% 55%, var(--card-mid) 0%, var(--card-dark) 70%, #111 100%);
  }
  .holder-name {
    position: absolute;
    left: 70px;
    top: 28px;
    margin: 0;
    font-family: "Francois One", sans-serif;
    font-weight: 400;
    font-size: 40px;
    line-height: 1;
    letter-spacing: 11px;
    color: var(--white);
  }
  .holder-name .surname { color: var(--accent); margin-left: 22px; }
  .holder-title {
    position: absolute;
    left: 70px;
    top: 76px;
    margin: 0;
    font-family: "Pathway Gothic One", sans-serif;
    font-size: 26px;
    letter-spacing: -0.6px;
    line-height: 1;
    color: var(--white);
  }
  .icon-strip {
    position: absolute;
    left: 36px;
    top: 124px;
    width: 56px;
    height: 138px;
    background: var(--accent);
  }
  .icon-strip svg {
    position: absolute;
    left: 14px;
    width: 26px;
    height: 26px;
    fill: none;
    stroke: var(--white);
    stroke-width: 2.4;
  }
  .contact-list {
    position: absolute;
    left: 96px;
    top: 136px;
    margin: 0;
    padding: 0;
    list-style: none;
    font-family: "Arimo", sans-serif;
    font-size: 14.5px;
    color: var(--white);
  }
  .contact-list li { height: 29px; line-height: 20px; }
  .contact-list li:nth-child(3) { height: 31px; }
  .band-rust, .band-accent, .band-cap {
    position: absolute;
    left: 0;
    top: 287px;
    width: 100%;
    border-radius: 0 0 48px 48px;
  }
  .band-rust {
    height: 239px;
    background: radial-gradient(ellipse at 65% 70%, var(--rust-light) 0%, #7a2c1a 45%, var(--rust-dark) 100%);
  }
  .band-accent {
    height: 139px;
    background: var(--accent);
  }
  .band-cap {
    height: 41px;
    background: linear-gradient(90deg, #1a1b1a, #393935 55%, #222321);
  }
  .divider-rule {
    position: absolute;
    left: 0;
    top: 281px;
    width: 100%;
    height: 6px;
    background: var(--rule);
  }
  .studio-name {
    position: absolute;
    left: 0;
    top: 327px;
    width: 100%;
    margin: 0;
    text-align: center;
    font-family: "Pinyon Script", cursive;
    font-size: 56px;
    line-height: 1;
    color: var(--ink);
  }
  .tagline {
    position: absolute;
    left: 0;
    top: 452px;
    width: 100%;
    margin: 0;
    text-align: center;
    font-family: "Pathway Gothic One", sans-serif;
    font-size: 44px;
    line-height: 1;
    color: var(--tagline);
  }
</style>
</head>
<body>
  <div class="business-card">
    <h1 class="holder-name">Omar<span class="surname">Haddad</span></h1>
    <p class="holder-title">Sr. Business Developement Manager</p>

    <div class="icon-strip">
      <svg style="top:14px" viewBox="0 0 26 26"><path d="M3 13 L13 4 L23 13 M6 11 V22 H20 V11 M11 22 V16 H15 V22"/></svg>
      <svg style="top:44px" viewBox="0 0 26 26"><circle cx="13" cy="13" r="10"/><path d="M3 13 H23 M13 3 C8 8 8 18 13 23 M13 3 C18 8 18 18 13 23"/></svg>
      <svg style="top:76px" viewBox="0 0 26 26"><rect x="3" y="6" width="20" height="14"/><path d="M3 6 L13 14 L23 6"/></svg>
      <svg style="top:104px" viewBox="0 0 26 26"><rect x="7" y="5" width="12" height="19" rx="3"/><path d="M10 5 V2 M9 10 H17"/><circle cx="13" cy="18" r="1.3"/></svg>
    </div>

    <ul class="contact-list">
      <li>P.O. Box 48210, Abu Dhabi,UAE</li>
      <li>www.lumerastudio.com</li>
      <li>Omar.haddad@lumeradesign.com</li>
      <li>00971&nbsp;&nbsp;&nbsp;55&nbsp;&nbsp;&nbsp;203&nbsp;&nbsp;&nbsp;6184</li>
    </ul>

    <div class="band-rust"></div>
    <div class="band-accent"></div>
    <div class="band-cap"></div>
    <div class="divider-rule"></div>

    <p class="studio-name">Lumera Creative Studio</p>
    <p class="tagline">Perosnify your business</p>
  </div>
</body>
</html>
```